Korean Homemade food restaurant just like what your mom cooks at home

I need a black and white simple and modern design according to my logo.
My restaurant name is Nal Som (meaning of home cooking).
I need to have 늘찬(Nal Som) in Korean need to be included. Once again 늘찬.
I am not sure if I need to include my name and number and adress.
Updates

늘찬 Nal Som 478 Harwell Rd. Larkmoor, WA 37118 Mark Yoon Owner Cell:555-608-2913 Store:555-617-3084

Target Market(s)

business owners, university students

Industry/Entity Type

Restaurant

Contact Information for Business Card

This is traditional Korean food restaurant that targets university students during lunch and Korean business travelers at dinner.

Font styles to use
Sans Serif

Requirements
Must have
• Must have my logo.

```html
<!DOCTYPE html>
<html lang="en">
<head>
<meta charset="utf-8">
<title>Nal Som — Business Card</title>
<link href="https://fonts.googleapis.com/css2?family=Noto+Sans+KR:wght@700;900&family=Questrial&family=Montserrat:wght@700&display=swap" rel="stylesheet">
<style>
  :root {
    --ink: #262626;
    --ink-deep: #1f1f1f;
    --paper: #ffffff;
    --backdrop: #ececec;
    --text-light: #f2f2f2;
  }
  * { box-sizing: border-box; margin: 0; padding: 0; }
  html, body {
    width: 1200px; height: 1000px; overflow: hidden;
    background: var(--backdrop);
    font-family: "Questrial", "Century Gothic", sans-serif;
  }
  .sheet {
    width: 1200px; height: 1000px;
    display: flex; flex-direction: column; align-items: center;
    justify-content: center; gap: 80px;
  }
  .card {
    position: relative; width: 700px; height: 400px;
    box-shadow: 0 10px 24px rgba(0,0,0,.18);
    overflow: hidden;
  }
  /* front */
  .card--front { background: var(--paper); }
  .card__diagonal { position: absolute; inset: 0; }
  .brand-mark {
    position: absolute; left: 56px; top: 70px;
    display: flex; align-items: center; gap: 12px;
  }
  .brand-mark__dot {
    width: 20px; height: 20px; border-radius: 50%; background: var(--ink);
  }
  .brand-mark__name {
    font-family: "Noto Sans KR", sans-serif; font-weight: 900;
    font-size: 60px; color: var(--ink); line-height: 1;
  }
  .contact {
    position: absolute; left: 470px; top: 168px;
    border-left: 1.5px solid var(--text-light);
    padding-left: 12px;
    color: var(--text-light);
    font-style: normal; font-size: 17px; line-height: 1.55;
    white-space: nowrap;
  }
  .contact strong { font-family: "Montserrat", sans-serif; font-weight: 700; font-size: 16px; }
  .contact .ko { font-family: "Noto Sans KR", sans-serif; font-weight: 700; font-size: 16px; }
  /* back */
  .card--back {
    background: var(--ink-deep);
    display: flex; align-items: center; justify-content: center;
  }
  .back-mark {
    display: flex; align-items: center; gap: 12px;
    color: var(--paper); font-size: 40px;
  }
  .back-mark__dot {
    width: 14px; height: 14px; border-radius: 50%; background: var(--paper);
  }
</style>
</head>
<body>
<main class="sheet">
  <section class="card card--front" aria-label="Business card front">
    <svg class="card__diagonal" width="700" height="400" viewBox="0 0 700 400" aria-hidden="true">
      <polygon points="0,400 590,0 700,0 700,400" fill="var(--ink)"/>
    </svg>
    <div class="brand-mark">
      <span class="brand-mark__dot"></span>
      <span class="brand-mark__name" lang="ko">늘찬</span>
    </div>
    <address class="contact">
      <div><span class="ko" lang="ko">늘찬</span> Nal <strong>Som</strong></div>
      <div><strong>Mark Yoon</strong> Owner</div>
      <div>Cell:555-608-2913</div>
      <div>Store:555-617-3084</div>
      <div>478 Harwell Rd.</div>
      <div>Larkmoor, WA 37118</div>
    </address>
  </section>

  <section class="card card--back" aria-label="Business card back">
    <div class="back-mark">
      <span class="back-mark__dot"></span>
      <span class="back-mark__name">Nal Som</span>
    </div>
  </section>
</main>
</body>
</html>
```